New Record Label needs a Web design

We are Moss Lantern: a London based, new & independent music production company aimed at the 25-40 age group. The musical style is Soul/Classic Motown.
We have at the moment just one signed artist, but will expand in the future.
We dont' have any webpage yet and are looking for an innovative web design for our webpage www.moss-lantern.com
I have uploaded our company logo.

Initially the whole website will only have 3 tabs: Home page/Artists/Contact

The design should be classic and high-end, but can be a bit crazy too.

```html
<!DOCTYPE html>
<html lang="en">
<head>
<meta charset="utf-8">
<title>Moss Lantern — Contact</title>
<link rel="stylesheet" href="https://fonts.googleapis.com/css2?family=Oswald:wght@300&family=Rokkitt:wght@700&display=swap">
<style>
  :root {
    --backdrop: #e9b8a1;
    --brand-red: #c83c3c;
    --deep-red: #6b1d20;
    --mid-red: #a62e30;
    --panel-tint: rgba(240, 225, 228, 0.72);
    --label-red: #a8242a;
    --white: #ffffff;
    --warm-amber: #e8a23a;
    --vinyl-dark: #2a160c;
    --grey-light: #e6e6e6;
    --grey-mid: #a9a9a9;
  }
  * { box-sizing: border-box; margin: 0; padding: 0; }
  html, body {
    width: 1200px; height: 1000px; overflow: hidden;
    background: var(--backdrop);
  }
  .page {
    position: relative; width: 1200px; height: 1000px;
    background: var(--backdrop);
  }
  .contact-card {
    position: absolute; left: 34px; top: 75px;
    width: 1133px; height: 850px; overflow: hidden;
    box-shadow: 0 2px 8px rgba(0,0,0,0.35);
  }
  .card-art { position: absolute; inset: 0; display: block; }

  .brand {
    position: absolute; left: 60px; top: 250px; width: 330px;
    display: flex; align-items: center; justify-content: center; gap: 14px;
  }
  .brand-dot {
    width: 26px; height: 26px; border-radius: 50%;
    background: var(--white);
  }
  .brand-name {
    font-family: "Rokkitt", Georgia, serif; font-weight: 700;
    font-size: 44px; color: var(--white); letter-spacing: 1px;
  }

  .contact-form {
    position: absolute; left: 540px; top: 157px; width: 568px;
  }
  .form-row { display: flex; align-items: flex-start; margin-bottom: 16px; }
  .form-label {
    width: 105px; padding-right: 11px; text-align: right;
    font-family: "Rokkitt", Georgia, serif; font-weight: 700;
    font-size: 20px; line-height: 26px; color: var(--label-red);
  }
  .form-field { width: 462px; height: 29px; background: var(--brand-red); }
  .form-field--comment { height: 180px; }

  .page-title {
    position: absolute; left: 10px; top: 558px;
    font-family: "Oswald", "Arial Narrow", sans-serif; font-weight: 300;
    font-size: 104px; line-height: 1; letter-spacing: 1px;
    color: transparent; -webkit-text-stroke: 2px var(--white);
  }
</style>
</head>
<body>
<main class="page">
  <section class="contact-card">
    <svg class="card-art" width="1133" height="850" viewBox="0 0 1133 850" aria-hidden="false">
      <defs>
        <linearGradient id="turntable-red" x1="0" y1="0" x2="1" y2="1">
          <stop offset="0" stop-color="#c23a3a"/>
          <stop offset="0.45" stop-color="#7a2225"/>
          <stop offset="1" stop-color="#c53d3d"/>
        </linearGradient>
        <linearGradient id="record-warm" x1="0" y1="0" x2="1" y2="1">
          <stop offset="0" stop-color="#f3c766"/>
          <stop offset="0.45" stop-color="#c97a22"/>
          <stop offset="1" stop-color="#2a160c"/>
        </linearGradient>
        <linearGradient id="platter-grey" x1="0" y1="0" x2="1" y2="0">
          <stop offset="0" stop-color="#9c9c9c"/>
          <stop offset="0.5" stop-color="#e4e4e4"/>
          <stop offset="1" stop-color="#cfcfcf"/>
        </linearGradient>
      </defs>
      <g role="img" aria-label="Red-tinted photo of a turntable with a vinyl record and tonearm">
        <rect x="0" y="0" width="1133" height="730" fill="url(#turntable-red)"/>
      </g>
      <polygon class="band-dark" points="0,0 640,0 411,490 0,490" fill="var(--deep-red)" opacity="0.55"/>
      <polygon class="form-panel" points="566,125 1133,125 1133,490 411,490" fill="var(--panel-tint)"/>
      <rect class="title-band" x="0" y="490" width="400" height="163" fill="var(--brand-red)"/>
      <polygon class="title-shadow" points="0,653 400,653 309,730 0,730" fill="var(--deep-red)"/>
      <polygon class="band-right" points="766,490 1133,490 1133,730 671,730" fill="var(--brand-red)" opacity="0.85"/>
      <g role="img" aria-label="Warm close-up photo of a vinyl record playing on a turntable">
        <polygon points="391,490 766,490 671,730 309,730" fill="url(#record-warm)"/>
      </g>
      <g role="img" aria-label="Blurred grey photo of a turntable platter edge">
        <rect x="0" y="730" width="1133" height="120" fill="url(#platter-grey)"/>
      </g>
    </svg>

    <div class="brand">
      <span class="brand-dot"></span>
      <span class="brand-name">Moss Lantern</span>
    </div>

    <form class="contact-form">
      <div class="form-row"><span class="form-label">Name:</span><div class="form-field"></div></div>
      <div class="form-row"><span class="form-label">e-mail:</span><div class="form-field"></div></div>
      <div class="form-row"><span class="form-label">Address:</span><div class="form-field"></div></div>
      <div class="form-row"><span class="form-label">Comment:</span><div class="form-field form-field--comment"></div></div>
    </form>

    <h1 class="page-title">CONTACT</h1>
  </section>
</main>
</body>
</html>
```